Business Card Vespalor - Accounting firm

Hi my friend.
I'm coming back to you to see if it would be possible for you to make a modern and minimalist business card design.
In shades of blue like the great logo you offered me.
The ideal is a modern and aesthetic business card.
The goal is to give a professional effect to the first exchanges.
Renewal and innovation in the accounting world !!
I thank you !!
Good evening to you

Target Market(s)

Young, dynamic and sensitive to marketing

Industry/Entity Type

Finance And Accounting

Contact Information for Business Card

Company logo and name. Last name, First name, Phone number, email address, company address, website.

Font styles to use
Sans Serif

Requirements
Must have
• The ideal is a modern and aesthetic business card.

Mentions to include: Company logo and name. Last name, First name, Phone number, email address, company address, website.
Nice to have
• The goal is to give a professional effect to the first exchanges.
Should not have
• Simplistic or childish design

```html
<!DOCTYPE html>
<html lang="en">
<head>
<meta charset="utf-8">
<title>Vespalor – Business Card</title>
<link rel="stylesheet" href="https://fonts.googleapis.com/css2?family=Montserrat:wght@400;500&display=swap">
<style>
  :root {
    --canvas-bg: #e8e8e8;
    --card-bg: #ffffff;
    --navy: #2f3461;
    --navy-deep: #2a2f5c;
    --petrol: #1f4f75;
    --ink-name: #2f3461;
    --ink-body: #6b6b72;
    --dot-1: #3a80c4;
    --dot-2: #3f8fc6;
    --dot-3: #4b9fc6;
    --dot-4: #5aaec3;
  }
  * { margin: 0; padding: 0; box-sizing: border-box; }
  html, body {
    width: 912px; height: 1200px; overflow: hidden;
    background: radial-gradient(ellipse at center, #f1f1f1 0%, var(--canvas-bg) 70%);
    font-family: "Montserrat", sans-serif;
  }
  .presentation { position: relative; width: 912px; height: 1200px; }
  .card {
    position: absolute; top: 498px;
    width: 339px; height: 203px;
    background: var(--card-bg);
    overflow: hidden;
    box-shadow: 0 1px 3px rgba(0,0,0,0.08);
  }
  .card--front { left: 81px; }
  .card--back { left: 491px; }
  .card__shape { position: absolute; inset: 0; width: 100%; height: 100%; }

  .brand {
    position: absolute; left: 72px; top: 84px;
    display: flex; align-items: center; gap: 9px;
  }
  .brand__dot {
    width: 26px; height: 26px; border-radius: 50%;
    background: var(--dot-4);
  }
  .brand__name {
    color: #ffffff; font-weight: 500; font-size: 34px;
    letter-spacing: -0.5px; line-height: 1;
  }

  .contact { position: absolute; left: 30px; top: 33px; }
  .contact__name {
    color: var(--ink-name); font-weight: 500; font-size: 12px;
    letter-spacing: 0.1px;
  }
  .contact__role {
    margin-top: 7px; margin-left: 3px;
    color: var(--ink-body); font-size: 7.4px; letter-spacing: 1.6px;
  }
  .contact__list { list-style: none; position: absolute; left: 0; top: 0; }
  .contact__item {
    position: absolute; left: 0; white-space: nowrap;
    color: var(--ink-body); font-size: 7.4px; line-height: 11px;
  }
  .contact__item::before {
    content: ""; position: absolute; left: 0; top: 1px;
    width: 10px; height: 10px; border-radius: 50%;
  }
  .contact__item span { display: block; padding-left: 19px; }
  .contact__item--phone { top: 46px; }
  .contact__item--phone::before { background: var(--dot-1); }
  .contact__item--mail { top: 68px; }
  .contact__item--mail::before { background: var(--dot-2); }
  .contact__item--web { top: 91px; }
  .contact__item--web::before { background: var(--dot-3); }
  .contact__item--address { top: 113px; }
  .contact__item--address::before { background: var(--dot-4); }
</style>
</head>
<body>
<main class="presentation">
  <section class="card card--front" aria-label="Business card front">
    <svg class="card__shape" viewBox="0 0 624 374" preserveAspectRatio="none" aria-hidden="true">
      <defs>
        <linearGradient id="front-band" x1="0" y1="1" x2="1" y2="0">
          <stop offset="0" stop-color="var(--navy)"/>
          <stop offset="0.55" stop-color="var(--navy-deep)"/>
          <stop offset="1" stop-color="var(--petrol)"/>
        </linearGradient>
      </defs>
      <path d="M276 0 H624 V226 L310 356 Q220 392 90 336 L0 282 V118 Z" fill="url(#front-band)"/>
    </svg>
    <div class="brand">
      <span class="brand__dot"></span>
      <span class="brand__name">Vespalor</span>
    </div>
  </section>

  <section class="card card--back" aria-label="Business card back">
    <svg class="card__shape" viewBox="0 0 624 374" preserveAspectRatio="none">
      <defs>
        <linearGradient id="back-panel" x1="0" y1="0" x2="1" y2="1">
          <stop offset="0" stop-color="var(--petrol)"/>
          <stop offset="0.5" stop-color="var(--navy)"/>
          <stop offset="1" stop-color="var(--navy)"/>
        </linearGradient>
      </defs>
      <rect role="img" aria-label="Decorative brand panel" x="336" y="0" width="288" height="374" rx="0" fill="url(#back-panel)"/>
    </svg>
    <div class="contact">
      <p class="contact__name">Your Name</p>
      <p class="contact__role">DESIGNATION</p>
      <ul class="contact__list" style="top:0">
        <li class="contact__item contact__item--phone"><span>+91 0123456789</span></li>
        <li class="contact__item contact__item--mail"><span>lorem.ipsum@lorem.com</span></li>
        <li class="contact__item contact__item--web"><span>www.loremipsum.com</span></li>
        <li class="contact__item contact__item--address"><span>Lorem Ipsum, Dummy text<br>Lorem Ipsum, Dummy text<br>ipsum industry 123456</span></li>
      </ul>
    </div>
  </section>
</main>
</body>
</html>
```